Brightwell Polar Systems Inc.
Business Card, Letter Head, Fax Cover, evelope and T-shirt
Bright & Fun-filled
Dorian Kestle
342 Harrowgate Ave
Bronx, NY, 10474
dkestle@bpsyst.example
www.Bpsyst.example
ill be using a clear plastic card, but also lets have the background as black.
Heating
Air Condition
Ventilation
Duct Work
Refrigeration
Solar, Geothermal
Design, Fabrication & Installation
Sales, Service & Repair

```html
<!DOCTYPE html>
<html lang="en">
<head>
<meta charset="utf-8">
<title>Brightwell Polar Systems Inc. – Business Card</title>
<link href="https://fonts.googleapis.com/css2?family=Cinzel:wght@400;600&family=Open+Sans:ital,wght@1,400&display=swap" rel="stylesheet">
<style>
:root{
  --bg:#d9d9d9;
  --card:#141414;
  --card-edge:#262626;
  --stripe-top:#38c6f0;
  --stripe-bottom:#0b6f9e;
  --rule:#5cb82e;
  --brand:#5cb82e;
  --name:#f0b02a;
  --text:#e6e6e6;
  --service:#f29a22;
  --bullet:#5cb82e;
  --web:#5cb82e;
  --web-back:#f2f2f2;
  --mark:#3a9bd0;
}
*{box-sizing:border-box;margin:0;padding:0}
html,body{width:1200px;height:862px;overflow:hidden}
body{background:var(--bg);position:relative;font-family:"Cinzel",serif}
.card{
  position:absolute;width:560px;height:330px;border-radius:26px;
  background:linear-gradient(160deg,#1d1d1d,var(--card) 60%);
  border:1px solid var(--card-edge);overflow:hidden;
  box-shadow:0 14px 30px rgba(0,0,0,.35);
}
.card--front{left:90px;top:70px}
.card--back{left:550px;top:460px}
.card__stripe{
  position:absolute;left:0;top:0;bottom:0;width:60px;
  background:linear-gradient(180deg,var(--stripe-top),var(--stripe-bottom));
}
.card__stripe::after{
  content:"";position:absolute;right:-5px;top:0;bottom:0;width:5px;background:var(--rule);
}
.brand{position:absolute;left:22px;top:26px;display:flex;align-items:center;gap:14px}
.brand__mark{width:78px;height:78px;border-radius:50%;background:var(--mark);flex:none}
.brand__name{
  color:var(--brand);font-family:"Cinzel",serif;font-weight:600;font-size:25px;line-height:1.15;letter-spacing:.5px;
}
.contact{position:absolute;left:110px;top:140px;color:var(--text)}
.contact__name{color:var(--name);font-size:20px;font-weight:400;margin-bottom:16px;letter-spacing:.5px}
.contact__address{font-size:12px;margin-bottom:10px}
.contact__list{list-style:none;font-size:12px}
.contact__list li{display:flex;align-items:center;gap:8px;height:17px}
.contact__list svg{width:11px;height:11px;fill:var(--service)}
.contact__web{color:var(--web);font-size:13px;margin-top:8px}
.services{
  position:absolute;left:110px;top:140px;list-style:none;
  font-family:"Open Sans",sans-serif;font-style:italic;font-size:14.5px;color:var(--service);line-height:27px;
}
.services span::before{content:"• ";color:var(--bullet)}
.services span{margin-right:6px}
.back__web{position:absolute;left:110px;top:280px;color:var(--web-back);font-size:17px;letter-spacing:.5px}
</style>
</head>
<body>

<section class="card card--front">
  <div class="card__stripe"></div>
  <div class="brand">
    <div class="brand__mark"></div>
    <div class="brand__name">Brightwell Polar<br>Systems Inc.</div>
  </div>
  <div class="contact">
    <h1 class="contact__name">Dorian Kestle</h1>
    <p class="contact__address">342 Harrowgate Ave. Bronx, NY. 10474</p>
    <ul class="contact__list">
      <li><svg viewBox="0 0 24 24"><path d="M6.6 10.8a15 15 0 0 0 6.6 6.6l2.2-2.2c.3-.3.7-.4 1-.2 1.1.4 2.3.6 3.6.6.6 0 1 .4 1 1V20c0 .6-.4 1-1 1A17 17 0 0 1 3 4c0-.6.4-1 1-1h3.5c.6 0 1 .4 1 1 0 1.3.2 2.5.6 3.6.1.3 0 .7-.2 1z"/></svg>718-555-0142</li>
      <li><svg viewBox="0 0 24 24"><path d="M7 1h10a2 2 0 0 1 2 2v18a2 2 0 0 1-2 2H7a2 2 0 0 1-2-2V3a2 2 0 0 1 2-2zm0 3v14h10V4z"/></svg>646-555-0187</li>
      <li><svg viewBox="0 0 24 24"><path d="M6 2h10v5H6zM3 8h18v10h-3v4H6v-4H3zm5 7v5h8v-5z"/></svg>718-555-0163</li>
      <li><svg viewBox="0 0 24 24"><path d="M2 5h20v14H2zm2 2v.5l8 5 8-5V7z"/></svg>dkestle@bpsyst.example</li>
    </ul>
    <p class="contact__web">www.Bpsyst.example</p>
  </div>
</section>

<section class="card card--back">
  <div class="card__stripe"></div>
  <div class="brand">
    <div class="brand__mark"></div>
    <div class="brand__name">Brightwell Polar<br>Systems Inc.</div>
  </div>
  <ul class="services">
    <li><span>Heating</span><span>Air Condition</span><span>Ventilation</span></li>
    <li><span>Duct Work</span><span>Refrigeration</span><span>Solar, Geothermal</span></li>
    <li><span>Design, Fabrication &amp; Installation</span></li>
    <li><span>Sales, Service &amp; Repair</span></li>
  </ul>
  <p class="back__web">www.Bpsyst.example</p>
</section>

</body>
</html>
```